Party Favors and Decorations Business Needs A Business Card Design

We are in need of a Logo design and business card design for a new small business called Willow Bay Designs. We create party decorations and favours for Bridal Showers, Baby Showers, Weddings Birthdays etc. This is a very personalized service based on Clients theme, colour, and style. We are looking for a high end elegant look. I have attached a file to the style I like including the type of paper.

Target Market(s)

women, young adults, expectant mothers, mothers

Industry/Entity Type

Small Business

Contact Information for Business Card

Willow Bay Designs Maple Cove, ON 519-806-4192 willowbaydesigns-example.ca danielle@willowbaygiftwrap-example.com find us on Friendlink

Logo Text

Willow Bay Designs

Font styles to use
Script

Requirements
Must have
• Name, email, web address, phone number
Should not have
• cutesy graphics

```html
<!DOCTYPE html>
<html lang="en">
<head>
<meta charset="utf-8">
<title>Willow Bay Designs – Business Card</title>
<link href="https://fonts.googleapis.com/css2?family=Kaushan+Script&family=Roboto+Condensed:wght@400&family=Arimo:wght@400&display=swap" rel="stylesheet">
<style>
  :root {
    --maroon: #4a0000;
    --orange: #ff5f00;
    --gold: #e2cf00;
    --amber: #d06a00;
    --mark: #f07810;
    --cloud: #ffffff;
    --cloud-edge: #cfd8d8;
    --white: #ffffff;
    --paper: #ffffff;
  }
  * { margin: 0; padding: 0; box-sizing: border-box; }
  html, body {
    width: 1200px;
    height: 353px;
    overflow: hidden;
    background: var(--paper);
  }
  .sheet {
    position: relative;
    width: 1200px;
    height: 353px;
  }
  .card {
    position: absolute;
    top: 0;
    width: 578px;
    height: 353px;
    overflow: hidden;
  }
  .card--front {
    left: 0;
    background: linear-gradient(90deg, var(--orange) 0%, #f58a00 45%, #ecb800 78%, var(--gold) 92%, var(--amber) 100%);
  }
  .card--back {
    left: 622px;
    background: var(--maroon);
  }
  .cloud {
    position: absolute;
    left: 0;
    top: 0;
  }
  .brand-dot {
    position: absolute;
    border-radius: 50%;
    background: var(--mark);
  }
  .card--front .brand-dot {
    width: 84px; height: 84px;
    left: 240px; top: 102px;
  }
  .card--back .brand-dot {
    width: 90px; height: 90px;
    left: 244px; top: 72px;
  }
  .brand-name {
    position: absolute;
    left: 0;
    width: 100%;
    text-align: center;
    font-family: "Kaushan Script", cursive;
    font-size: 24px;
    line-height: 1;
  }
  .card--front .brand-name {
    width: 564px;
    top: 222px;
    color: var(--maroon);
  }
  .card--back .brand-name {
    top: 196px;
    color: var(--white);
  }
  .footer-band {
    position: absolute;
    left: 0;
    bottom: 0;
    width: 100%;
    height: 65px;
    background: var(--maroon);
  }
  .footer-label {
    position: absolute;
    top: 19px;
    font-family: "Arimo", Arial, sans-serif;
    font-size: 21px;
    color: var(--white);
  }
  .footer-label--name { left: 76px; }
  .footer-label--phone { left: 430px; }
  .contact {
    position: absolute;
    left: 0;
    top: 243px;
    width: 100%;
    text-align: center;
    font-family: "Roboto Condensed", "Arial Narrow", sans-serif;
    font-size: 15.5px;
    line-height: 24px;
    color: var(--white);
  }
</style>
</head>
<body>
<main class="sheet">
  <section class="card card--front" aria-label="Business card front">
    <svg class="cloud" width="578" height="353" viewBox="0 0 578 353" aria-hidden="true">
      <path fill="var(--cloud)" stroke="var(--cloud-edge)" stroke-width="10" stroke-linejoin="round"
        d="M 70 280 C 47 280 38 262 38 240 L 38 215 C 38 172 70 142 105 134 C 100 102 130 80 165 82 C 180 47 215 30 255 30 C 295 30 320 47 332 72 C 350 57 380 54 405 67 C 425 77 432 95 430 107 C 470 107 505 132 515 167 C 535 187 535 230 525 255 C 518 272 505 280 490 280 Z"/>
    </svg>
    <span class="brand-dot" aria-hidden="true"></span>
    <p class="brand-name">Willow Bay Designs</p>
    <div class="footer-band">
      <span class="footer-label footer-label--name">Name</span>
      <span class="footer-label footer-label--phone">Phone</span>
    </div>
  </section>

  <section class="card card--back" aria-label="Business card back">
    <span class="brand-dot" aria-hidden="true"></span>
    <p class="brand-name">Willow Bay Designs</p>
    <p class="contact">
      Willow Bay Designs Maple Cove, ON 519-806-4192 willowbaydesigns-example.ca<br>
      danielle@willowbaygiftwrap-example.com, find us on Friendlink
    </p>
  </section>
</main>
</body>
</html>
```